Candle Labels for Pillar Candles with Stone Heart Pendants

Graphic designer to create visuals for customer for product labeling .

We're looking for a talented graphic designer to redesign candle labels for pillar candles that will be wrapped with stone hearts.
There are 10 different versions

- Experience with software [e.g. Adobe Illustrator, Adobe InDesign, Adobe Photoshop, etc.]
- Relevant experience [e.g. level of expertise, knowledge of specific industry, etc.]

File size should be 6.75" (w) X 4.75" (h).
Full color.
See samples of what we have below.
Stones include:
Amethyst
Black Obsidian
Rose Quartz
Lapis
Rhodonite
Aventurine
Tiger Eye
Turquoise
White Howlite
Hematite

Images of what we have currently are attached to this posting.

Requirements
Must have
• This project should have a "New Age" feel and appeal to persons of eclecticism and self-spirituality.

```html
<!DOCTYPE html>
<html lang="en">
<head>
<meta charset="UTF-8">
<title>Healing Stone Pillar Candle Labels</title>
<link rel="stylesheet" href="https://fonts.googleapis.com/css2?family=Playfair+Display:wght@700;800&family=Montserrat:wght@500;600&display=swap">
<style>
  :root {
    --canvas-bg: #ecebe8;
    --label-white: #ffffff;
    --rose: #f0859f;
    --rose-deep: #e8758f;
    --lapis: #5555ad;
    --lapis-deep: #3a3a9a;
    --obsidian: #3a3a3a;
    --obsidian-deep: #262626;
    --rhodonite: #d8435c;
    --rhodonite-deep: #c0203c;
    --amethyst: #b070c8;
    --amethyst-deep: #9a50b4;
    --ink-light: #ffffff;
  }
  * { box-sizing: border-box; margin: 0; padding: 0; }
  html, body { width: 1200px; height: 916px; overflow: hidden; }
  body {
    background: var(--canvas-bg);
    position: relative;
  }
  .label-row {
    position: absolute;
    left: 87px;
    top: 200px;
    display: flex;
    gap: 43px;
  }
  .label {
    position: relative;
    width: 169px;
    height: 515px;
    background: var(--label-white);
    overflow: hidden;
    box-shadow: 0 2px 8px rgba(0,0,0,0.08);
  }
  .label-shapes {
    position: absolute;
    inset: 0;
    width: 100%;
    height: 100%;
  }
  .stone-name {
    position: absolute;
    left: 0;
    right: 0;
    top: var(--name-top, 100px);
    text-align: center;
    font-family: "Playfair Display", serif;
    font-weight: 800;
    font-size: var(--name-size, 36px);
    line-height: 0.95;
    color: var(--ink-light);
    letter-spacing: -0.5px;
  }
  .stone-tagline {
    position: absolute;
    left: 0;
    right: 0;
    top: 228px;
    text-align: center;
    font-family: "Montserrat", sans-serif;
    font-weight: 500;
    font-size: 12.5px;
    line-height: 1.6;
    color: var(--ink-light);
    text-transform: uppercase;
  }
  .floral-art {
    position: absolute;
    left: 20px;
    top: 292px;
    width: 129px;
    height: 138px;
    border-radius: 50% 50% 40% 40%;
    background: radial-gradient(circle at 50% 50%, rgba(255,255,255,0.75), rgba(255,255,255,0.35) 70%, rgba(255,255,255,0) 100%);
  }
  .burn-time {
    position: absolute;
    left: 0;
    right: 0;
    bottom: 22px;
    text-align: center;
    font-family: "Montserrat", sans-serif;
    font-weight: 600;
    font-size: 12px;
    letter-spacing: 0.2px;
    color: var(--accent-deep);
  }
  .label--rose { --accent: var(--rose); --accent-deep: var(--rose-deep); --name-size: 35px; --name-top: 78px; }
  .label--lapis { --accent: var(--lapis); --accent-deep: var(--lapis-deep); --name-size: 38px; --name-top: 98px; }
  .label--obsidian { --accent: var(--obsidian); --accent-deep: var(--obsidian-deep); --name-size: 33px; --name-top: 80px; }
  .label--rhodonite { --accent: var(--rhodonite); --accent-deep: var(--rhodonite-deep); --name-size: 27px; --name-top: 104px; }
  .label--amethyst { --accent: var(--amethyst); --accent-deep: var(--amethyst-deep); --name-size: 28px; --name-top: 102px; }
  .label--obsidian .burn-time { color: #333333; }
</style>
</head>
<body>
  <main class="label-row">
    <article class="label label--rose">
      <svg class="label-shapes" viewBox="0 0 310 945" preserveAspectRatio="none" aria-hidden="true">
        <polygon points="0,102 310,52 310,72 0,124" fill="var(--rose)"/>
        <path d="M0,150 L310,88 L310,745 C220,770 90,810 0,865 Z" fill="var(--rose)"/>
      </svg>
      <h2 class="stone-name">Rose<br>Quartz</h2>
      <p class="stone-tagline">Spiritual growth &amp;<br>healing stone</p>
      <div class="floral-art" role="img" aria-label="White floral ornament with leaves and blossoms"></div>
      <p class="burn-time">50 HR BURN TIME</p>
    </article>

    <article class="label label--lapis">
      <svg class="label-shapes" viewBox="0 0 310 945" preserveAspectRatio="none" aria-hidden="true">
        <polygon points="0,102 310,52 310,72 0,124" fill="var(--lapis)"/>
        <path d="M0,150 L310,88 L310,745 C220,770 90,810 0,865 Z" fill="var(--lapis)"/>
      </svg>
      <h2 class="stone-name">Lapis</h2>
      <p class="stone-tagline">Spiritual growth &amp;<br>healing stone</p>
      <div class="floral-art" role="img" aria-label="White floral ornament with leaves and blossoms"></div>
      <p class="burn-time">50 HR BURN TIME</p>
    </article>

    <article class="label label--obsidian">
      <svg class="label-shapes" viewBox="0 0 310 945" preserveAspectRatio="none" aria-hidden="true">
        <polygon points="0,102 310,52 310,72 0,124" fill="var(--obsidian)"/>
        <path d="M0,150 L310,88 L310,745 C220,770 90,810 0,865 Z" fill="var(--obsidian)"/>
      </svg>
      <h2 class="stone-name">Black<br>Obsidian</h2>
      <p class="stone-tagline">Spiritual growth &amp;<br>healing stone</p>
      <div class="floral-art" role="img" aria-label="White floral ornament with leaves and blossoms"></div>
      <p class="burn-time">50 HR BURN TIME</p>
    </article>

    <article class="label label--rhodonite">
      <svg class="label-shapes" viewBox="0 0 310 945" preserveAspectRatio="none" aria-hidden="true">
        <polygon points="0,102 310,52 310,72 0,124" fill="var(--rhodonite)"/>
        <path d="M0,150 L310,88 L310,745 C220,770 90,810 0,865 Z" fill="var(--rhodonite)"/>
      </svg>
      <h2 class="stone-name">Rhodonite</h2>
      <p class="stone-tagline">Spiritual growth &amp;<br>healing stone</p>
      <div class="floral-art" role="img" aria-label="White floral ornament with leaves and blossoms"></div>
      <p class="burn-time">50 HR BURN TIME</p>
    </article>

    <article class="label label--amethyst">
      <svg class="label-shapes" viewBox="0 0 310 945" preserveAspectRatio="none" aria-hidden="true">
        <polygon points="0,102 310,52 310,72 0,124" fill="var(--amethyst)"/>
        <path d="M0,150 L310,88 L310,745 C220,770 90,810 0,865 Z" fill="var(--amethyst)"/>
      </svg>
      <h2 class="stone-name">Amethyst</h2>
      <p class="stone-tagline">Spiritual growth &amp;<br>healing stone</p>
      <div class="floral-art" role="img" aria-label="White floral ornament with leaves and blossoms"></div>
      <p class="burn-time">50 HR BURN TIME</p>
    </article>
  </main>
</body>
</html>
```